need web page design for BrinkwellHub.com

This site sells information products for international corporate users. It is selling Harbor Ledgers and Tariff Routines, a product on international business tax, and other books. See sample. I will also upload a possible logo. Upload 2 The tag line is Predicting and Solving Business and Law Issues for the Multinational Upload 3 is a sample theme from Shopify, the site I will use. The sample is for ideas only. I am not wedded to it. Upload 4 is Cobalt Ledger Monthly Pge

```html
<!DOCTYPE html>
<html lang="en">
<head>
<meta charset="utf-8">
<title>BrinkwellHub.com</title>
<link href="https://fonts.googleapis.com/css2?family=Questrial&family=Open+Sans:wght@400;600&display=swap" rel="stylesheet">
<style>
:root{
  --navy:#0d2a6b;
  --navy-deep:#082056;
  --nav-top:#0b3c8f;
  --nav-bottom:#05276a;
  --ink:#333;
  --muted:#6a6a6a;
  --icon:#6f6f6f;
  --line:#dedede;
  --panel:rgba(70,70,70,.82);
  --paper:#fff;
}
*{box-sizing:border-box;margin:0;padding:0}
html,body{width:992px;height:1200px;overflow:hidden;background:var(--paper)}
body{position:relative;font-family:"Open Sans",Arial,sans-serif;color:var(--ink)}

.brand{position:absolute;left:124px;top:34px}
.brand-name{font-family:"Questrial",Arial,sans-serif;font-size:25px;color:var(--navy);line-height:1}
.brand-tag{font-size:7px;color:#555;margin-top:5px;letter-spacing:.1px}

.nav{position:absolute;left:0;top:96px;width:992px;height:40px;background:linear-gradient(var(--nav-top),var(--nav-bottom));display:flex;justify-content:center}
.nav a{font-family:"Questrial",Arial,sans-serif;color:#fff;text-decoration:none;font-size:14px;line-height:40px;padding:0 18px}

.hero{position:absolute;left:0;top:136px;width:992px;height:385px;background:linear-gradient(180deg,#a9c4de 0%,#d6e2ec 30%,#b3a49a 48%,#8d8a82 62%,#7e95a4 72%,#566e7c 100%)}
.hero-arrow{position:absolute;top:146px}
.signup{position:absolute;left:644px;top:69px;width:232px;height:219px;background:var(--panel);padding:22px 22px 0 23px;color:#fff}
.signup h2{font-family:"Questrial",Arial,sans-serif;font-weight:400;font-size:18px;line-height:23px}
.signup p{font-size:9px;line-height:14px;margin-top:4px;color:#eee}
.signup .field{width:188px;height:23px;background:#fff;margin-top:7px;font-size:9px;color:#777;padding:6px 9px}
.signup .field:first-of-type{margin-top:8px}
.signup .submit{display:inline-block;margin-top:10px;background:var(--navy-deep);color:#fff;font-weight:600;font-size:11.5px;width:84px;height:26px;line-height:26px;text-align:center}
.dots{position:absolute;left:460px;top:366px;display:flex;gap:3px}
.dots i{width:9px;height:9px;border-radius:50%;background:#fff}

.about{position:absolute;left:160px;top:548px;width:672px;text-align:center}
.about h1{font-family:"Questrial",Arial,sans-serif;font-weight:400;font-size:24px;color:#333}
.about p{font-size:10px;line-height:16px;color:#666;margin-top:8px}

.feature{position:absolute;top:674px;display:flex;gap:8px}
.feature .ico{width:59px;height:59px;border-radius:50%;background:var(--icon);display:flex;align-items:center;justify-content:center;flex:none}
.feature h3{font-family:"Questrial",Arial,sans-serif;font-weight:400;font-size:16.5px;color:#555;margin-top:2px}
.feature p{font-size:9.6px;line-height:15px;color:#777;margin-top:3px;width:100px}
.rule{position:absolute;left:123px;top:765px;width:751px;height:1px;background:var(--line)}

.card{position:absolute;top:801px;width:245px;height:253px;border:1px solid #e4e4e4;background:linear-gradient(#fff 60%,#f6f6f6);padding:14px 15px 0}
.card .photo{width:218px;height:103px}
.card h2{font-family:"Questrial",Arial,sans-serif;font-weight:400;font-size:19px;color:var(--navy);margin-top:9px}
.card p{font-size:9.6px;line-height:16px;color:#777;margin-top:4px}
.btn{display:inline-block;background:var(--navy-deep);color:#fff;font-size:10px;font-weight:600;width:90px;height:27px;line-height:27px;text-align:center;border-radius:2px;margin-top:10px}
.stories{padding-right:12px}
.stories h2{margin-top:8px;font-size:20px}
.stories h4{font-weight:400;font-size:10.5px;color:#333;margin-top:13px}
.stories h4+p{margin-top:2px;font-size:9.2px}
.stories .btn{margin-top:20px}

.footer{position:absolute;left:0;top:1100px;width:992px;height:100px;border-top:1px solid var(--line)}
.footer nav{position:absolute;left:123px;top:24px;font-family:"Questrial",Arial,sans-serif;font-size:12.5px;color:#333}
.footer nav span{margin:0 5px}
.footer small{position:absolute;left:123px;top:51px;font-size:9.5px;color:#555}
.social{position:absolute;left:799px;top:24px;display:flex;gap:6px}
.social i{width:17px;height:17px;display:block}
</style>
</head>
<body>

<header class="brand">
  <div class="brand-name">BrinkwellHub.com</div>
  <div class="brand-tag">Practical Guidance on Cross-Border Trade, Tax and Law for Growing Companies</div>
</header>

<nav class="nav">
  <a>Home</a><a>About Us</a><a>Featrured Tax</a><a>Foregin Investment</a><a>News &amp; Media</a><a>Blog</a><a>Contact</a>
</nav>

<section class="hero" role="img" aria-label="City skyline with towers and an arched bridge reflected in a river">
  <svg class="hero-arrow" style="left:36px" width="28" height="66" viewBox="0 0 28 66"><path d="M26 2 L3 33 L26 64" fill="none" stroke="#fff" stroke-width="1.5"/></svg>
  <svg class="hero-arrow" style="left:918px" width="28" height="66" viewBox="0 0 28 66"><path d="M2 2 L25 33 L2 64" fill="none" stroke="#fff" stroke-width="1.5"/></svg>
  <div class="signup">
    <h2>Get the Most Important News Stories</h2>
    <p>Etiam est nunc venenatis in tristique eu imperdiet ac nisl Cum sociis natoq</p>
    <div class="field">Your Name</div>
    <div class="field">Email address</div>
    <span class="submit">SUBMIT</span>
  </div>
  <div class="dots"><i></i><i></i><i></i><i></i></div>
</section>

<section class="about">
  <h1>Littl About Brinkwell Hub</h1>
  <p>Mauris vel lacus vitae felis vestibulum volutpat Etiam est nunc venenatis in tristique eu imperdiet ac nisl Cum sociis natoque penatibus et magnis dis parturient montes nascetur ridiculus mus In iaculis facilisis massa Etiam eu urna Sed porta Suspendisse quam leo molestie sed luctus quis feugiat in pede Fusce tellus Sed metus augue convallis et vehicula ut pulvinar eu ante Integer orci tellus tristiqu</p>
</section>

<div class="feature" style="left:127px">
  <div class="ico"><svg width="30" height="34" viewBox="0 0 30 34"><rect x="3" y="2" width="24" height="30" rx="2" fill="none" stroke="#fff" stroke-width="2.5"/><path d="M8 10h14M8 15h14M8 20h8M8 25h8" stroke="#fff" stroke-width="2"/><text x="18" y="28" fill="#fff" font-size="10" font-family="Arial">$</text></svg></div>
  <div><h3>Featured Tax</h3><p>Etiam est nunc vene natis in tristique</p></div>
</div>
<div class="feature" style="left:319px">
  <div class="ico"><svg width="38" height="34" viewBox="0 0 38 34"><path d="M19 3v27M9 32h20M5 7h28" stroke="#fff" stroke-width="2.5"/><path d="M5 7 L1 19h8z M33 7 L29 19h8z" fill="none" stroke="#fff" stroke-width="1.5"/><path d="M0 19a5 4 0 0 0 10 0zM28 19a5 4 0 0 0 10 0z" fill="#fff"/></svg></div>
  <div><h3>Featured Law</h3><p>Etiam est nunc vene natis in tristique</p></div>
</div>
<div class="feature" style="left:514px">
  <div class="ico"><svg width="38" height="36" viewBox="0 0 38 36"><circle cx="21" cy="15" r="13" fill="none" stroke="#fff" stroke-width="2.5"/><path d="M21 7v8l6 4" fill="none" stroke="#fff" stroke-width="2"/><ellipse cx="11" cy="24" rx="9" ry="3" fill="#fff"/><ellipse cx="11" cy="29" rx="9" ry="3" fill="#fff"/><ellipse cx="11" cy="33" rx="9" ry="3" fill="#fff"/></svg></div>
  <div><h3>Investments</h3><p>Etiam est nunc vene natis in tristique</p></div>
</div>
<div class="feature" style="left:698px">
  <div class="ico"><span style="color:#fff;font-size:36px;font-weight:600;line-height:1">$</span></div>
  <div><h3>Finance</h3><p>Etiam est nunc vene natis in tristique</p></div>
</div>

<div class="rule"></div>

<article class="card" style="left:119px">
  <div class="photo" role="img" aria-label="Three colleagues reviewing documents at a desk" style="background:linear-gradient(90deg,#6d6a6a,#c9c3bd 45%,#8ba0c0)"></div>
  <h2>Latest Informations</h2>
  <p>Etiam est nunc venenatis in tristique eu imperdiet ac nisl Cum sociis natoque penatibus et magnis dis parturient montes nascetur</p>
  <span class="btn">READ MORE</span>
</article>

<article class="card" style="left:373px">
  <div class="photo" role="img" aria-label="Hands holding a tablet showing blue financial charts" style="background:linear-gradient(135deg,#d9e6f2,#5d8fc4 55%,#1f4f8f)"></div>
  <h2>What We Do</h2>
  <p>Etiam est nunc venenatis in tristique eu imperdiet ac nisl Cum sociis natoque penatibus et magnis dis parturient montes nascetur</p>
  <span class="btn">READ MORE</span>
</article>

<article class="card stories" style="left:625px;padding-left:21px">
  <h2>Latest Top Stories</h2>
  <h4>Etiam est nunc venenatis</h4>
  <p>in tristique eu imperdiet ac nisl Cum sociis natoque penatibus et magnis dis</p>
  <h4>Ut nisi erat fermentum vel congue</h4>
  <p>Morbi diam mauris viverra in gravida eu mattis in ante Morbi eget arcu Morbi porta libero id ullamcorper nonummy nibh ligula</p>
  <span class="btn">VIEW MORE</span>
</article>

<footer class="footer">
  <nav>Home<span>|</span>About Us<span>|</span>Featrured Tax<span>|</span>Foregin Investment<span>|</span>News &amp; Media<span>|</span>Blog<span>|</span>Contact</nav>
  <small>© 2014 Company Name&nbsp; All right reserved&nbsp; Term of Use</small>
  <div class="social"><i style="background:#3b5998"></i><i style="background:#55b7e6"></i><i style="background:#0e6aa8"></i></div>
</footer>

</body>
</html>
```